Word template Letterhead for Australian Law Firm

We are a small law firm based in Manly, NSW, Australia. We have had a new logo designed for us and wish to freshen up the appearance of our letterhead. We require the letterhead to be in a word document that we can type over. This will not be a ‘printed’ letterhead because we send the majority of our correspondence via email. We would like to see a few options. We have attached our previous letterhead as well as the artwork for our new logo. We like the idea of a watermark across the bottom of the letter but the watermark must stay in place and we must be able to type over it. We are open to some colour throughout the letterhead because the majority of our correspondence is sent electronically. We also use electronic signatures. I have uploaded an example of this.The letterhead must include:-1. Our address details – including our phone number, physical address, website address etc. These details can be found on the copy of our previous letterhead;2. ABN Number;3. The words ‘Brevicor (NSW) Pty Ltd ACN 482 731 058 trading as Shipton & AssociatesLiability limited by a scheme approved under Professional Standards Legislation. The letterhead does not need to include the names and qualifications of the people working at the firm. Thank you.

Target Market(s)

Clients and other parties

Industry/Entity Type

Law Firm

Font styles to use
Other font styles liked:
• raleway, montserrat

Colors

Designer to choose colors to be used in the design.

Requirements
Must have
• Certain wording - please see project description.
• Must be a word document and must be able to type over the watermark etc.
Nice to have
• Watermark at the bottom of the letter.

```html
<!DOCTYPE html>
<html lang="en">
<head>
<meta charset="utf-8">
<title>Kervell &amp; Associates — Letterhead Options</title>
<link href="https://fonts.googleapis.com/css2?family=Montserrat:ital,wght@0,400;0,500;0,600;1,400&display=swap" rel="stylesheet">
<style>
  :root {
    --backdrop: #fafafa;
    --paper: #ffffff;
    --paper-edge: #dcdde3;
    --brand-blue: #4d58a3;
    --brand-gold: #c5a96f;
    --ink-dark: #26283a;
    --wash-blue: #e9ebf4;
    --wash-gold: #f6f2e8;
  }
  * { box-sizing: border-box; margin: 0; padding: 0; }
  html, body {
    width: 1200px; height: 912px; overflow: hidden;
    background: var(--backdrop);
    font-family: "Montserrat", Arial, sans-serif;
  }
  .stage { position: relative; width: 1200px; height: 912px; }

  .letterhead {
    position: absolute;
    width: 478px; height: 676px;
    background: var(--paper);
    border: 1px solid var(--paper-edge);
    overflow: hidden;
  }
  .letterhead--rule-top { left: 74px; top: 62px; }
  .letterhead--split-top { left: 630px; top: 156px; }

  .firm-name {
    position: absolute; top: 74px;
    transform: translateX(-50%);
    display: flex; align-items: center; gap: 5px;
    font-size: 8.6px; font-weight: 600; letter-spacing: 0.07em;
    color: var(--ink-dark); white-space: nowrap;
  }
  .firm-name__dot {
    width: 7px; height: 7px; border-radius: 50%;
    background: var(--brand-blue);
  }
  .letterhead--rule-top .firm-name { left: 100px; }
  .letterhead--split-top .firm-name { left: 377px; }

  .contact {
    position: absolute; top: 31px;
    text-align: right;
    font-size: 6px; line-height: 8.6px;
    color: var(--brand-blue); letter-spacing: 0.03em;
    white-space: nowrap;
  }
  .letterhead--rule-top .contact { right: 50px; }
  .letterhead--split-top .contact { right: 204px; }
  .contact__group + .contact__group { margin-top: 3px; }
  .contact__label { color: var(--brand-gold); }
  .contact__web { margin-top: 2.5px; }

  .header-rule {
    position: absolute; left: 0; right: 0; top: 116px;
    height: 1.7px; background: var(--brand-blue);
  }
  .divider { position: absolute; top: 0; width: 1.6px; }
  .divider--blue { left: 298px; height: 127px; background: var(--brand-blue); }
  .divider--gold { left: 304px; height: 107px; background: var(--brand-gold); }

  .watermark-area {
    position: absolute; left: 186px; top: 500px;
    width: 292px; height: 152px;
    background: linear-gradient(160deg, rgba(233,235,244,0) 0%, var(--wash-blue) 45%, var(--wash-gold) 100%);
    opacity: 0.8;
  }

  .legal {
    position: absolute; right: 95px; top: 627px;
    text-align: right;
    font-size: 7px; line-height: 9.3px;
    color: var(--brand-blue); letter-spacing: 0.02em;
    white-space: nowrap;
  }
  .legal__liability { font-style: italic; }

  .accreditation {
    position: absolute; left: 396px; top: 621px;
    width: 32px; height: 32px; border-radius: 50%;
    border: 1.4px solid var(--ink-dark);
  }
</style>
</head>
<body>
<main class="stage">

  <section class="letterhead letterhead--rule-top" aria-label="Letterhead option with horizontal rule">
    <div class="firm-name"><span class="firm-name__dot"></span>Kervell &amp; Associates</div>
    <address class="contact">
      <div class="contact__group">SUITE 4, 12 CORSAIR LANE<br>FAIRHAVEN, NSW 2097</div>
      <div class="contact__group">
        <span class="contact__label">TELEPHONE:</span> (02) 5550 4812<br>
        <span class="contact__label">FACSIMILE:</span> (02) 5550 4813<br>
        <span class="contact__label">EMAIL:</span> reception@brevicorlaw.com.au<br>
        ABN: 31 482 731 058
      </div>
      <div class="contact__web">www.kervellassociates.com.au</div>
    </address>
    <div class="header-rule"></div>
    <div class="watermark-area" role="img" aria-label="Faint flowing wave watermark across the bottom of the page"></div>
    <p class="legal">
      Brevicor (NSW) Pty Ltd ACN 482 731 058 trading as Kervell &amp; Associates<br>
      <span class="legal__liability">Liability limited by a scheme approved under Professional Standards Legislation</span>
    </p>
    <div class="accreditation"></div>
  </section>

  <section class="letterhead letterhead--split-top" aria-label="Letterhead option with vertical dividers">
    <address class="contact">
      <div class="contact__group">SUITE 4, 12 CORSAIR LANE<br>FAIRHAVEN, NSW 2097</div>
      <div class="contact__group">
        <span class="contact__label">TELEPHONE:</span> (02) 5550 4812<br>
        <span class="contact__label">FACSIMILE:</span> (02) 5550 4813<br>
        <span class="contact__label">EMAIL:</span> reception@brevicorlaw.com.au<br>
        ABN: 31 482 731 058
      </div>
      <div class="contact__web">www.kervellassociates.com.au</div>
    </address>
    <div class="divider divider--blue"></div>
    <div class="divider divider--gold"></div>
    <div class="firm-name"><span class="firm-name__dot"></span>Kervell &amp; Associates</div>
    <div class="watermark-area" role="img" aria-label="Faint flowing wave watermark across the bottom of the page"></div>
    <p class="legal">
      Brevicor (NSW) Pty Ltd ACN 482 731 058 trading as Kervell &amp; Associates<br>
      <span class="legal__liability">Liability limited by a scheme approved under Professional Standards Legislation</span>
    </p>
    <div class="accreditation"></div>
  </section>

</main>
</body>
</html>
```